Small consulting business needs logo and business card design

I need a logo, business card and letterhead design for a small consulting firm called Kestrawell Consulting. My customers are generally small to medium sized businesses but I have done work for major corporates and government departments. The field of consulting is strategic/business planning and program management. I have blue as the predominate colour in my current business card but I am happy to change this for the right design
Industry/Entity Type
Business

```html
<!DOCTYPE html>
<html lang="en">
<head>
<meta charset="utf-8">
<title>Kestrawell Consulting – Stationery</title>
<link href="https://fonts.googleapis.com/css2?family=Montserrat:wght@400;500;700&display=swap" rel="stylesheet">
<style>
  :root {
    --backdrop: #707070;
    --paper: #ffffff;
    --navy: #123f86;
    --sky: #1f8fd6;
    --ink: #3a3a3a;
    --muted: #8a8a8a;
    --envelope: #3c3c3e;
    --envelope-flap: #333335;
  }
  * { box-sizing: border-box; margin: 0; padding: 0; }
  html, body {
    width: 1200px; height: 900px; overflow: hidden;
    background: var(--backdrop);
    font-family: "Montserrat", sans-serif;
    color: var(--ink);
  }
  .stationery { position: relative; width: 1200px; height: 900px; }

  .brand-name {
    display: inline-flex; align-items: center; gap: 8px;
    font-weight: 700; color: var(--navy);
    letter-spacing: 0.02em; white-space: nowrap;
  }
  .brand-dot { width: 0.9em; height: 0.9em; border-radius: 50%; background: var(--sky); flex: none; }

  /* Letterhead */
  .letterhead {
    position: absolute; left: 70px; top: 55px;
    width: 560px; height: 790px;
    background: var(--paper);
    padding: 48px 52px;
    box-shadow: 0 6px 18px rgba(0,0,0,0.25);
    overflow: hidden;
  }
  .letterhead-header { display: flex; justify-content: space-between; align-items: flex-start; }
  .letterhead .brand-name { font-size: 19px; margin-top: 44px; }
  .letterhead-contact {
    border-left: 1px solid #cfcfcf; padding-left: 10px;
    font-size: 9px; line-height: 1.7; color: var(--muted);
  }
  .letterhead-contact .accent { color: var(--navy); }
  .letterhead-contact li { list-style: none; display: flex; align-items: center; gap: 5px; }
  .bullet { width: 6px; height: 6px; background: var(--sky); flex: none; }
  .letter-body { margin: 56px 0 0 70px; width: 360px; font-size: 9.5px; line-height: 1.75; }
  .letter-body p { margin-bottom: 12px; }
  .sign-off { margin: 34px 0 0 70px; font-size: 9.5px; line-height: 1.8; }
  .sign-line { width: 90px; border-bottom: 1px solid #9aa; margin: 18px 0 4px; }
  .letterhead-corner {
    position: absolute; right: 0; bottom: 0;
    width: 170px; height: 170px;
  }

  /* Envelopes */
  .envelope {
    position: absolute; width: 500px; height: 240px;
    background: var(--envelope);
    box-shadow: 0 6px 16px rgba(0,0,0,0.3);
    overflow: hidden;
  }
  .envelope--top { left: 660px; top: 55px; }
  .envelope--bottom { left: 660px; top: 605px; }
  .envelope-flap { position: absolute; inset: 0; }
  .envelope-label {
    position: absolute; right: 36px; bottom: 40px;
    width: 230px; height: 70px;
    background: var(--paper); border-radius: 6px;
    display: flex; align-items: center; justify-content: center;
  }
  .envelope-label .brand-name { font-size: 15px; }

  /* Business cards */
  .business-card {
    position: absolute; width: 240px; height: 138px;
    padding: 16px 16px;
    box-shadow: 0 5px 14px rgba(0,0,0,0.3);
    font-size: 8px; line-height: 1.6;
  }
  .business-card--front { left: 660px; top: 330px; background: var(--navy); color: #fff; }
  .business-card--back { left: 920px; top: 330px; background: var(--paper); color: var(--ink); }
  .business-card .brand-name { font-size: 12px; }
  .business-card--front .brand-name { color: #fff; }
  .card-details { display: flex; justify-content: space-between; margin-top: 26px; }
  .card-person strong { font-weight: 500; }
  .card-contact { list-style: none; }
  .card-contact li { display: flex; align-items: center; gap: 4px; }
  .card-contact .bullet { width: 5px; height: 5px; }
  .business-card--front .card-band { position: absolute; left: 0; right: 0; top: 46px; height: 2px; background: var(--sky); }
  .business-card--back .card-band { position: absolute; left: 0; right: 0; top: 46px; height: 2px; background: var(--navy); }
</style>
</head>
<body>
<main class="stationery">

  <section class="letterhead" aria-label="Letterhead">
    <header class="letterhead-header">
      <div class="brand-name"><span class="brand-dot"></span>Kestrawell Consulting</div>
      <ul class="letterhead-contact">
        <li>Office address to be confirmed</li>
        <li class="accent"><span class="bullet"></span>Mobile No. (TBA Later)</li>
        <li class="accent"><span class="bullet"></span>Email address (TBA Later)</li>
        <li class="accent"><span class="bullet"></span>Web address (TBA Later)</li>
      </ul>
    </header>

    <div class="letter-body">
      <p>Dear Client,</p>
      <p>Thank you for the opportunity to support your planning work this year. Our team reviewed the goals you shared and prepared a clear outline of next steps for your program.</p>
      <p>We propose a short workshop with your leaders, followed by a written plan that sets priorities, owners and dates. Each stage will be tracked so progress stays visible to everyone.</p>
      <p>Please let us know a suitable time to meet and confirm the scope.</p>
    </div>

    <div class="sign-off">
      <div>Yours sincerely,</div>
      <div class="sign-line"></div>
      <div>Director</div>
    </div>

    <svg class="letterhead-corner" viewBox="0 0 170 170" aria-hidden="true">
      <rect x="70" y="70" width="100" height="100" fill="#123f86"/>
    </svg>
  </section>

  <section class="envelope envelope--top" aria-label="Envelope">
    <svg class="envelope-flap" viewBox="0 0 500 240" preserveAspectRatio="none" aria-hidden="true">
      <polygon points="0,0 500,0 500,18 0,18" fill="#333335"/>
    </svg>
    <div class="envelope-label"><div class="brand-name"><span class="brand-dot"></span>Kestrawell Consulting</div></div>
  </section>

  <article class="business-card business-card--front" aria-label="Business card front">
    <div class="brand-name"><span class="brand-dot"></span>Kestrawell Consulting</div>
    <div class="card-band"></div>
    <div class="card-details">
      <div class="card-person">
        <div><strong>Name:</strong> Your Name</div>
        <div><strong>Title:</strong> Principal Consultant</div>
      </div>
      <ul class="card-contact">
        <li><span class="bullet"></span>Mobile No. (TBA Later)</li>
        <li><span class="bullet"></span>Email address (TBA Later)</li>
        <li><span class="bullet"></span>Web address (TBA Later)</li>
      </ul>
    </div>
  </article>

  <article class="business-card business-card--back" aria-label="Business card back">
    <div class="brand-name"><span class="brand-dot"></span>Kestrawell Consulting</div>
    <div class="card-band"></div>
    <div class="card-details">
      <div class="card-person">
        <div><strong>Name:</strong> Your Name</div>
        <div><strong>Title:</strong> Principal Consultant</div>
      </div>
      <ul class="card-contact">
        <li><span class="bullet"></span>Mobile No. (TBA Later)</li>
        <li><span class="bullet"></span>Email address (TBA Later)</li>
        <li><span class="bullet"></span>Web address (TBA Later)</li>
      </ul>
    </div>
  </article>

  <section class="envelope envelope--bottom" aria-label="Envelope">
    <svg class="envelope-flap" viewBox="0 0 500 240" preserveAspectRatio="none" aria-hidden="true">
      <polygon points="0,0 500,0 460,60 40,60" fill="#333335"/>
    </svg>
    <div class="envelope-label"><div class="brand-name"><span class="brand-dot"></span>Kestrawell Consulting</div></div>
  </section>

</main>
</body>
</html>
```